Clean and modern business cards

Looking for an updated business card design for my dental office “corvanta dental” . Looking for a modern clean / sleek design . I’m thinking black background but open to seeing other options . One side needs to have an appointment card . Card needs to have logo, dentist name , phone, email , address . I’ve attached couple of cards I thought were cool as well as my logo
Target Market(s)
Dental patients
Industry/Entity Type
Dentistry
Contact Information for Business Card
Phone email address

```html
<!DOCTYPE html>
<html lang="en">
<head>
<meta charset="utf-8">
<title>Corvanta Dental – Business Card</title>
<link href="https://fonts.googleapis.com/css2?family=Montserrat:wght@400;500&display=swap" rel="stylesheet">
<style>
  :root {
    --page-bg: #cdccc8;
    --card-bg: #000000;
    --ink: #ffffff;
    --field: #f3f3f1;
    --muted: #d9d9d9;
  }
  * { box-sizing: border-box; margin: 0; padding: 0; }
  html, body {
    width: 1200px; height: 900px; overflow: hidden;
    background: var(--page-bg);
    font-family: "Montserrat", sans-serif;
    color: var(--ink);
  }
  .sheet { position: relative; width: 1200px; height: 900px; }
  .card {
    position: absolute; left: 268px; width: 664px; height: 380px;
    background: var(--card-bg);
    box-shadow: 0 6px 18px rgba(0,0,0,.18);
  }
  .card--front { top: 50px; }
  .card--back { top: 470px; }

  /* brand */
  .brand { display: flex; align-items: center; gap: 16px; position: absolute; }
  .brand__dot { border-radius: 50%; background: var(--ink); flex: none; }
  .brand__name {
    font-weight: 500; text-transform: uppercase; letter-spacing: .12em;
    color: var(--ink); white-space: nowrap;
  }
  .card--front .brand { left: 50%; top: 92px; transform: translateX(-50%); }
  .card--front .brand__dot { width: 54px; height: 54px; }
  .card--front .brand__name { font-size: 30px; }

  .doctor-name {
    position: absolute; top: 196px; left: 0; right: 0; text-align: center;
    font-size: 22px; font-weight: 400; letter-spacing: .12em; text-transform: uppercase;
  }
  .contact-row {
    position: absolute; top: 280px; left: 0; right: 0;
    display: flex; justify-content: center; align-items: center; gap: 30px;
    font-size: 16px; letter-spacing: .05em; color: var(--muted);
  }
  .contact-row__divider { width: 1px; height: 40px; background: var(--muted); transform: rotate(25deg); }

  /* appointment side */
  .card--back .brand { right: 34px; top: 26px; gap: 8px; }
  .card--back .brand__dot { width: 18px; height: 18px; }
  .card--back .brand__name { font-size: 11px; }

  .appointment__title {
    position: absolute; left: 46px; top: 72px;
    font-size: 28px; font-weight: 400; letter-spacing: .14em; text-transform: uppercase;
  }
  .field-row { position: absolute; left: 46px; right: 46px; display: flex; align-items: center; gap: 18px; }
  .field-row__label { font-size: 16px; letter-spacing: .05em; width: 72px; flex: none; }
  .field-row__label--inline { width: auto; margin-left: 14px; }
  .field-row__box { height: 30px; background: var(--field); flex: 1; }
  .field-row--name { top: 140px; }
  .field-row--date { top: 196px; }
  .field-row--details { top: 252px; }

  .day-options {
    position: absolute; left: 136px; right: 46px; top: 318px;
    display: flex; justify-content: space-between;
  }
  .day-option { display: flex; align-items: center; gap: 6px; font-size: 10px; }
  .day-option__box { width: 13px; height: 13px; background: var(--field); }
</style>
</head>
<body>
<main class="sheet">
  <section class="card card--front" aria-label="Business card front">
    <div class="brand">
      <span class="brand__dot"></span>
      <span class="brand__name">Corvanta Dental</span>
    </div>
    <h1 class="doctor-name">Doctor Name</h1>
    <div class="contact-row">
      <span>Phone Number</span>
      <span class="contact-row__divider"></span>
      <span>Email</span>
      <span class="contact-row__divider"></span>
      <span>Address</span>
    </div>
  </section>

  <section class="card card--back" aria-label="Appointment card">
    <div class="brand">
      <span class="brand__dot"></span>
      <span class="brand__name">Corvanta Dental</span>
    </div>
    <h2 class="appointment__title">Appointment</h2>
    <div class="field-row field-row--name">
      <span class="field-row__label">Name</span>
      <span class="field-row__box"></span>
    </div>
    <div class="field-row field-row--date">
      <span class="field-row__label">Date</span>
      <span class="field-row__box"></span>
      <span class="field-row__label field-row__label--inline">Time</span>
      <span class="field-row__box"></span>
    </div>
    <div class="field-row field-row--details">
      <span class="field-row__label">Details</span>
      <span class="field-row__box"></span>
    </div>
    <div class="day-options">
      <span class="day-option"><span class="day-option__box"></span>Mon</span>
      <span class="day-option"><span class="day-option__box"></span>Mon</span>
      <span class="day-option"><span class="day-option__box"></span>Mon</span>
      <span class="day-option"><span class="day-option__box"></span>Mon</span>
      <span class="day-option"><span class="day-option__box"></span>Mon</span>
      <span class="day-option"><span class="day-option__box"></span>Mon</span>
    </div>
  </section>
</main>
</body>
</html>
```